Graphic Design Project

I need to create a graphic design, which needs to be editable for me in Powerpoint... I have attached it a draft of it, but I need to be able to change the text of it. I want it to look more professional

Target Market(s)

Business Executives

Industry/Entity Type

Graphic Design

Requirements
Must have
• Make it look professional; the colors can change; I just need to be able to edit the text in powerpoint or either word

```html
<!DOCTYPE html>
<html lang="en">
<head>
<meta charset="utf-8">
<title>IT Vision &amp; Leadership Framework</title>
<link rel="stylesheet" href="https://fonts.googleapis.com/css2?family=Open+Sans:wght@400;600;700&display=swap">
<style>
  :root {
    --paper: #ece7dc;
    --paper-light: #f5f2eb;
    --paper-edge: #ddd6c8;
    --ink: #111111;
    --purple: #7b4fa6;
    --purple-dark: #5a3584;
    --purple-light: #a784c9;
    --green: #8cbc3a;
    --green-dark: #5f8f1e;
    --green-light: #b6d97a;
    --red: #c8343a;
    --red-dark: #941c22;
    --red-light: #e57a7e;
    --blue: #2f6fbd;
    --blue-dark: #1d4c8c;
    --blue-light: #74a6de;
  }
  * { box-sizing: border-box; margin: 0; padding: 0; }
  html, body { width: 1200px; height: 1000px; overflow: hidden; }
  body {
    font-family: "Open Sans", Arial, sans-serif;
    color: var(--ink);
    background:
      radial-gradient(ellipse at 50% 45%, var(--paper-light) 0%, var(--paper) 60%, var(--paper-edge) 100%);
  }
  .framework { position: relative; width: 1200px; height: 1000px; }

  .pillar { position: absolute; width: 192px; height: 122px; }
  .pillar__back {
    position: absolute; left: -22px; top: -20px; width: 192px; height: 122px;
    border-radius: 11px;
    background: linear-gradient(180deg, var(--c-light) 0%, var(--c) 45%, var(--c-dark) 100%);
    box-shadow: 2px 3px 5px rgba(0,0,0,0.25);
  }
  .pillar__front {
    position: absolute; inset: 0;
    border-radius: 11px;
    border: 1.5px solid var(--c-light);
    background: linear-gradient(180deg, rgba(255,255,255,0.97) 0%, rgba(250,248,250,0.93) 55%, rgba(240,238,240,0.9) 100%);
    box-shadow: 3px 4px 7px rgba(0,0,0,0.2);
    display: flex; align-items: center; justify-content: center;
    text-align: center; line-height: 1.2;
    font-size: 24px; font-weight: 600; padding: 6px;
  }
  .pillar--purple { --c: var(--purple); --c-dark: var(--purple-dark); --c-light: var(--purple-light); }
  .pillar--green  { --c: var(--green);  --c-dark: var(--green-dark);  --c-light: var(--green-light); }
  .pillar--red    { --c: var(--red);    --c-dark: var(--red-dark);    --c-light: var(--red-light); }
  .pillar--blue   { --c: var(--blue);   --c-dark: var(--blue-dark);   --c-light: var(--blue-light); }

  .label--title { font-size: 27px; font-weight: 700; line-height: 1.3; }
  .label--regular { font-weight: 400; font-size: 24px; }
  .label--large { font-size: 31px; font-weight: 700; }
  .label--small { font-size: 20px; line-height: 1.9; }
  .label--compact { font-size: 21px; line-height: 1.3; }

  .foundation {
    position: absolute; left: 154px; top: 788px; width: 888px; height: 69px;
    border-radius: 9px;
    background: linear-gradient(180deg, var(--purple-light) 0%, var(--purple) 40%, var(--purple-dark) 100%);
    border: 1.5px solid var(--purple-light);
    box-shadow: 4px 8px 10px rgba(0,0,0,0.28);
    display: flex; align-items: center; justify-content: center;
    color: #ffffff; font-size: 30px; font-weight: 700; letter-spacing: 0.5px;
  }
</style>
</head>
<body>
<main class="framework">
  <div class="pillar pillar--purple" style="left:521px;top:163px">
    <div class="pillar__back"></div>
    <div class="pillar__front label--title">IT VISION &amp;<br>LEADERSHIP</div>
  </div>

  <div class="pillar pillar--green" style="left:406px;top:324px">
    <div class="pillar__back"></div>
    <div class="pillar__front label--regular">Maintain IT<br>Operational<br>Excellence</div>
  </div>
  <div class="pillar pillar--green" style="left:641px;top:324px">
    <div class="pillar__back"></div>
    <div class="pillar__front">Create<br>Business<br>Value</div>
  </div>

  <div class="pillar pillar--red" style="left:296px;top:485px">
    <div class="pillar__back"></div>
    <div class="pillar__front label--large">Transform<br>IT Team</div>
  </div>
  <div class="pillar pillar--red" style="left:531px;top:485px">
    <div class="pillar__back"></div>
    <div class="pillar__front">Master<br>Relationship<br>Management</div>
  </div>
  <div class="pillar pillar--red" style="left:760px;top:485px">
    <div class="pillar__back"></div>
    <div class="pillar__front">Market &amp;<br>Communicate<br>Value</div>
  </div>

  <div class="pillar pillar--blue" style="left:184px;top:646px">
    <div class="pillar__back"></div>
    <div class="pillar__front">Customer<br>Engagement<br>Model</div>
  </div>
  <div class="pillar pillar--blue" style="left:408px;top:646px">
    <div class="pillar__back"></div>
    <div class="pillar__front label--small">Service-Minded<br>IT Culture</div>
  </div>
  <div class="pillar pillar--blue" style="left:637px;top:646px">
    <div class="pillar__back"></div>
    <div class="pillar__front label--compact">Policy, Process<br>&amp;<br>Methodologies</div>
  </div>
  <div class="pillar pillar--blue" style="left:867px;top:646px">
    <div class="pillar__back"></div>
    <div class="pillar__front label--large" style="font-size:29px">Meaningful<br>Metrics</div>
  </div>

  <div class="foundation">MANAGING CHANGE</div>
</main>
</body>
</html>
```